Jewellery Shop of 20 over years needs a new Business Card

We need a new business card that is refreshing, trendy for our Jewellery shop. We carry mid to high end fine jewellery. We want the design of the new business card to be clean cut, refreshing and different. Please try to keep to using the same logo we have, and for more information on the company you can check us out on www.corallisjewels.com.sg or on https://www.facebook.com/Corallisjewelcrafts/

Target Market(s)

late 20s to 50s

Industry/Entity Type

Jewelry Store

Contact Information for Business Card

Marlow's Jewel Crafts Co Pte Ltd
517 Tessaly Road, #02-14/15 Varnel Plaza Singapore 241093
Tel: (65) 64927150 Fax:( 65) 64927281 WhatsApp: ( 65) 90461358
Email: marlowtay@quillnet.com.sg
Website: www.corallisjewels.com.sg

Marlow Tay
Gemologist/Designer/Founder since 1980

Font styles to use
Serif

Requirements
Must have
• Trendy, Classic Clean Look
Should not have
• Should not be too dull or old looking, should not look like my old business card, no photos of jewellery

```html
<!DOCTYPE html>
<html lang="en">
<head>
<meta charset="utf-8">
<title>Marlow's Jewel Crafts – Business Card</title>
<link href="https://fonts.googleapis.com/css2?family=Cinzel:wght@400;600&family=Lato:wght@400;700&display=swap" rel="stylesheet">
<style>
  :root {
    --stage: #1e1e1f;
    --paper: #fbfbfa;
    --ink: #55575b;
    --gold: #c9a45a;
    --gold-deep: #b08a3e;
    --gold-bright: #e2bf54;
    --card-black: #121212;
  }
  * { margin: 0; padding: 0; box-sizing: border-box; }
  html, body {
    width: 1200px; height: 873px; overflow: hidden;
    background: var(--stage);
  }
  .canvas {
    position: relative; width: 1200px; height: 873px;
    display: flex; align-items: center; justify-content: center; gap: 40px;
  }
  .card {
    position: relative; width: 520px; height: 297px;
    border-radius: 4px; overflow: hidden;
    box-shadow: 0 14px 30px rgba(0,0,0,.55);
  }

  /* front */
  .card-front { background: var(--paper); font-family: "Lato", sans-serif; }
  .front-mark {
    position: absolute; left: 30px; top: 108px; width: 210px;
    text-align: center;
    font-family: "Cinzel", serif; font-weight: 600;
    font-size: 22px; line-height: 1.2; color: var(--gold);
  }
  .front-divider {
    position: absolute; left: 262px; top: 64px; width: 1.5px; height: 120px;
    background: linear-gradient(var(--gold), rgba(201,164,90,0));
  }
  .contact {
    position: absolute; left: 290px; top: 58px;
  }
  .contact-name {
    font-weight: 700; font-size: 17px; color: var(--gold); letter-spacing: .2px;
  }
  .contact-title {
    font-size: 11.5px; color: var(--ink); margin-top: 3px; margin-bottom: 16px;
  }
  .contact-list { list-style: none; }
  .contact-list li {
    display: flex; align-items: center; gap: 9px;
    font-size: 11.5px; color: var(--ink); height: 19px;
  }
  .contact-list svg { width: 11px; height: 11px; fill: var(--gold); flex: none; }
  .contact-web { color: var(--gold) !important; padding-left: 20px; }
  .front-address {
    position: absolute; left: 30px; bottom: 22px;
    font-size: 11px; color: var(--gold); letter-spacing: .3px;
  }
  .front-band {
    position: absolute; right: 0; bottom: 44px; width: 200px; height: 12px;
    background: var(--gold); border-top-left-radius: 12px;
  }
  .front-edge {
    position: absolute; left: 0; right: 0; bottom: 0; height: 6px;
    background: #e6e6e6;
  }

  /* back */
  .card-back {
    background: radial-gradient(ellipse at 50% 40%, #1d1d1d 0%, var(--card-black) 75%);
    text-align: center;
  }
  .back-mark {
    position: absolute; left: 0; right: 0; top: 96px;
    font-family: "Cinzel", serif; font-weight: 600;
    font-size: 32px; color: var(--gold-bright); letter-spacing: 1px;
  }
  .back-company {
    position: absolute; left: 0; right: 0; bottom: 54px;
    font-family: "Cinzel", serif; font-weight: 400;
    font-size: 15px; letter-spacing: 1.5px; color: var(--gold-deep);
  }
</style>
</head>
<body>
<main class="canvas">
  <section class="card card-front" aria-label="Business card front">
    <div class="front-mark">Marlow's<br>Jewel Crafts</div>
    <div class="front-divider"></div>
    <div class="contact">
      <p class="contact-name">Marlow Tay</p>
      <p class="contact-title">Gemologist &amp; Designer</p>
      <ul class="contact-list">
        <li>
          <svg viewBox="0 0 12 12" aria-hidden="true"><path d="M1 3c0-1 1-2 2-2l1.5 2.5-1 1c.6 1.5 1.5 2.4 3 3l1-1L10 8c0 1-1 2-2 2C4 10 1 7 1 3z"/></svg>
          +65 6492 7150
        </li>
        <li>
          <svg viewBox="0 0 12 12" aria-hidden="true"><path d="M3 1h6v3H3zM1 5h10v5H9V8H3v2H1zM3.5 9h5v2h-5z"/></svg>
          +65 6492 7281
        </li>
        <li>
          <svg viewBox="0 0 12 12" aria-hidden="true"><path d="M1 2.5h10v7H1zM1.5 3l4.5 3.5L10.5 3v1L6 7.5 1.5 4z" fill-rule="evenodd"/></svg>
          marlowtay@quillnet.com.sg
        </li>
        <li class="contact-web">www.quillnet.com.sg</li>
      </ul>
    </div>
    <div class="front-band"></div>
    <p class="front-address">517 Tessaly Road #02-14 Varnel Plaza, Singapore 241093</p>
    <div class="front-edge"></div>
  </section>

  <section class="card card-back" aria-label="Business card back">
    <div class="back-mark">Marlow's Jewel Crafts</div>
    <p class="back-company">MARLOW'S JEWEL CRAFTS CO PTE LTD</p>
  </section>
</main>
</body>
</html>
```